Volmira Logo and business card

We need a business card and logo, we are currently using a logo that we like but would like to be a bit more streamlined. We deal with very high end clients and our business card needs to reflect that. We would love to see and hire somebody that can deliver a very MODERN, simple design. With he main front of the card to be black with either a red lettering or White to provide great contrast. I would like to have a minimalist abstract picture of a heavy machine on it but it is not a requirement ( most likely an Crane ( a bold heron crane with a bucket would be perfect or maybe a vendari 270 XT )) If it keeps in line with being a classic simple, and modern design. Letterpress is also an option where it gives it a great look and texture, the card will be printed on a thick stock. On the back there needs to be a star included somewhere on the card and design, this represents the first generation that started the company back in 1936 therefore it is a sentimental addition ( make it modern and simple)
We do not want a cheesy construction template. We do heavy site work, aka we use excavators, payloaders, off road rok j40 trucks, very big fun toys.
There is a huge chance to get the web design as well for the winning design.
Have fun, cannot wait to see the designs!
In addition, we'd like to point out that our primary need and priority is still the BUSINESS CARD design itself. The logo has to complement the overall look of the business card, but it is secondary to the card's look. Please keep this in mind.
Thank you,
Gerald
Target Market(s)
General Contractors, upscale home owners ( house values of 1M plus)
and commercial property owners.
Projects range from $5000 to 1 million.
Industry/Entity Type
Construction
Requirements
Must have
- Star incorporated into design
Nice to have
- an abstract heavy site work machine ( pics attached) If it keeps in line with being a classic simple, and modern design.
I would like to have black and red on the design since all the lettering on the trucks is red, but i will let the designer take care of that.

```html
<!DOCTYPE html>
<html lang="en">
<head>
<meta charset="utf-8">
<title>Volmira Industries – Business Card</title>
<link rel="stylesheet" href="https://fonts.googleapis.com/css2?family=Ubuntu:wght@400;500;700&display=swap">
<style>
  :root {
    --page-bg: #e7e4e0;
    --card-black: #0b0b0c;
    --brand-red: #e8232d;
    --band-black: #141414;
    --ink-white: #ffffff;
    --photo-sky: #b9c6d3;
    --photo-green: #6f7d55;
    --photo-earth: #8a7a5c;
  }
  * { margin: 0; padding: 0; box-sizing: border-box; }
  html, body {
    width: 1200px; height: 900px; overflow: hidden;
    background: var(--page-bg);
    font-family: "Ubuntu", sans-serif;
  }
  .stage {
    width: 1200px; height: 900px;
    display: flex; align-items: center; justify-content: center; gap: 60px;
  }
  .card {
    width: 500px; height: 286px;
    border-radius: 4px; overflow: hidden; position: relative;
    box-shadow: 0 6px 18px rgba(0,0,0,.18);
  }
  .card-front { background: var(--card-black); }
  .front-wordmark {
    position: absolute; left: 44px; bottom: 48px;
    color: var(--brand-red); font-weight: 500; line-height: 1;
  }
  .front-wordmark .name { font-size: 58px; letter-spacing: 1px; display: block; }
  .front-wordmark .suffix { font-size: 17px; letter-spacing: 2px; display: block; margin-top: 8px; }
  .card-back svg { display: block; }
  .back-text { font-family: "Ubuntu", sans-serif; fill: var(--ink-white); }
  .back-wordmark { font-family: "Ubuntu", sans-serif; font-weight: 700; fill: var(--band-black); }
</style>
</head>
<body>
<main class="stage">
  <section class="card card-front" aria-label="Card front">
    <div class="front-wordmark">
      <span class="name">Volmira</span>
      <span class="suffix">INDUSTRIES INC.</span>
    </div>
  </section>

  <section class="card card-back" aria-label="Card back">
    <svg width="500" height="286" viewBox="0 0 500 286" xmlns="http://www.w3.org/2000/svg">
      <defs>
        <linearGradient id="photoTone" x1="0" y1="0" x2="1" y2="1">
          <stop offset="0" stop-color="var(--photo-sky)"/>
          <stop offset=".45" stop-color="var(--photo-green)"/>
          <stop offset="1" stop-color="var(--photo-earth)"/>
        </linearGradient>
      </defs>
      <rect class="photo-collage" width="500" height="286" fill="url(#photoTone)" role="img" aria-label="Collage of photos of excavators, dump trucks and bulldozers on work sites"/>
      <path class="red-field" fill="var(--brand-red)"
        d="M0,100 C30,92 50,84 80,84 C110,84 120,74 150,72 C180,70 190,60 220,58 C250,56 260,48 300,46 C340,44 350,36 390,36 C430,36 450,28 480,28 L500,28 L500,286 L0,286 Z"/>
      <path class="red-field-edge" fill="none" stroke="#fff" stroke-width="3"
        d="M0,100 C30,92 50,84 80,84 C110,84 120,74 150,72 C180,70 190,60 220,58 C250,56 260,48 300,46 C340,44 350,36 390,36 C430,36 450,28 480,28 L500,28"/>
      <rect class="name-band" x="0" y="160" width="500" height="42" fill="var(--band-black)"/>
      <text class="back-wordmark" x="22" y="140" font-size="28">Volmira</text>
      <polygon class="heritage-star" fill="#fff"
        points="80,171 88.2,193.7 112.3,194.5 93.3,209.3 100,232.5 80,219 60,232.5 66.7,209.3 47.7,194.5 71.8,193.7"/>
      <text class="back-text" x="232" y="100" font-size="13">Building No, Street No,</text>
      <text class="back-text" x="232" y="117" font-size="13">City, State, ZipCode</text>
      <text class="back-text" x="232" y="180" font-size="16" font-weight="500" letter-spacing="1">ALEX MORENO</text>
      <text class="back-text" x="232" y="196" font-size="12">Designation</text>
      <text class="back-text" x="232" y="226" font-size="13">+123 555 0142</text>
      <text class="back-text" x="232" y="246" font-size="13">alexmoreno@mail.com</text>
    </svg>
  </section>
</main>
</body>
</html>
```